We need a Facebook ad design for mobile app business.

"VANTORO" app platform providing a range of services like home massage therapy or home hair cut needs 4 Facebook advertisement designs to hire the service providers. Each ad needs to bold one the professions and also show the others professions!! let say we we need one design emphasizing on Massage Therapist, one for hair stylists, one for tune up technicians, and that includes 4 professions : house keepers + lawn mowers, snow blowers and tutors. Each one of the designs requires a different content.
This app is gonna lunch in Thunder Bay/ON/Canada, So it is necessary to be mentioned. And even a design must be included the pandemic situation for some professions and EARNING A SIDE INCOME UP TO 50K PER YEAR AND ALSO TO BE YOUR OWN BOSS!.
Vantoro is service application that provides different ranges of services like automotive service, home cleaning, massage therapy and etc. So the design must be a very nice combination of services and very clear.

To get better understanding of the app please check it in the google play store or app store through following links:
https://apps.kelvamarket.example/details?id=com.vantorojobs

• Apply green, silver and golden colors

```html
<!DOCTYPE html>
<html lang="en">
<head>
<meta charset="utf-8">
<title>Vantoro – Hiring Now Ads</title>
<link href="https://fonts.googleapis.com/css2?family=Montserrat:wght@400;600;700;800;900&display=swap" rel="stylesheet">
<style>
  :root {
    --page: #ececec;
    --white: #ffffff;
    --green-light: #22c83f;
    --green: #14b334;
    --green-dark: #0c7f25;
    --gold-light: #f1dc8e;
    --gold: #c9a544;
    --gold-dark: #8d6d1c;
    --black: #050505;
    --ink: #1b1b1b;
  }
  * { box-sizing: border-box; margin: 0; padding: 0; }
  html, body {
    width: 1200px; height: 1200px; overflow: hidden;
    background: var(--page);
    font-family: "Montserrat", Arial, sans-serif;
  }
  .ad-sheet { position: relative; width: 1200px; height: 1200px; }
  .ad {
    position: absolute; width: 475px; height: 475px; overflow: hidden;
    background: var(--white);
  }
  .ad--massage { left: 102px; top: 75px; }
  .ad--hair    { left: 671px; top: 75px; }
  .ad--tutors  { left: 102px; top: 619px; }
  .ad--home    { left: 671px; top: 619px; }

  .ad__shapes { position: absolute; inset: 0; width: 475px; height: 475px; }

  .phone {
    position: absolute; left: 59px; top: 31px; width: 104px; height: 212px;
    background: var(--black); border-radius: 14px;
  }
  .phone__speaker {
    position: absolute; top: 11px; left: 38px; width: 28px; height: 2px;
    background: #555; border-radius: 2px;
  }
  .phone__screen {
    position: absolute; left: 4px; right: 4px; top: 23px; bottom: 23px;
    background: var(--white);
  }
  .phone__button {
    position: absolute; bottom: 5px; left: 45px; width: 14px; height: 14px;
    border-radius: 50%; background: #2c2c2c;
  }
  .brand { position: absolute; left: 0; right: 0; top: 52px; text-align: center; }
  .brand__dot {
    display: block; width: 36px; height: 36px; border-radius: 50%;
    background: var(--green); margin: 0 auto 6px;
  }
  .brand__name { font-weight: 800; font-size: 16px; color: var(--green); letter-spacing: 0.5px; }

  /* Headline: every line placed on its own row */
  .headline { position: absolute; left: 0; top: 0; width: 282px; height: 475px; font-weight: 900; }
  .headline__line {
    position: absolute; left: 0; right: 0; text-align: center; white-space: nowrap;
    line-height: 1; color: var(--white); font-weight: 900;
  }
  .headline__kicker { color: var(--ink); font-weight: 400; }

  .ad--massage .headline__kicker { top: 266px; font-size: 24px; letter-spacing: 3px; }
  .ad--massage .headline__line--1 { top: 288px; font-size: 42px; }
  .ad--massage .headline__line--2 { top: 325px; font-size: 42px; }

  .ad--hair .headline__kicker { top: 255px; font-size: 22px; letter-spacing: 2.5px; }
  .ad--hair .headline__line--1 { top: 272px; font-size: 73px; }
  .ad--hair .headline__line--2 { top: 334px; font-size: 40px; }

  .ad--tutors .headline__kicker { top: 273px; font-size: 24px; letter-spacing: 2.5px; }
  .ad--tutors .headline__line--1 { top: 296px; font-size: 25px; }
  .ad--tutors .headline__line--2 { top: 320px; font-size: 48px; }

  .ad--home .headline__line { text-align: left; left: 32px; right: auto; }
  .ad--home .headline__kicker { top: 273px; font-size: 24px; letter-spacing: 2.5px; }
  .ad--home .headline__line--1 { top: 300px; font-size: 19.5px; }
  .ad--home .headline__line--2 { top: 324px; font-size: 19.5px; }
  .ad--home .headline__line--3 { top: 350px; font-size: 19.5px; }

  .at-home {
    position: absolute; height: 32px; border-radius: 16px;
    background: linear-gradient(180deg, var(--gold-light), var(--gold) 55%, var(--gold-dark));
    color: var(--ink); font-weight: 900; font-size: 26px; line-height: 32px; text-align: center;
    white-space: nowrap;
  }
  .ad--massage .at-home { left: 17px; top: 370px; width: 248px; }
  .ad--hair .at-home    { left: 26px; top: 379px; width: 229px; height: 30px; line-height: 30px; font-size: 24px; }
  .ad--tutors .at-home  { left: 26px; top: 379px; width: 229px; height: 30px; line-height: 30px; font-size: 24px; }
  .ad--home .at-home    { left: 26px; top: 382px; width: 188px; height: 25px; line-height: 25px; font-size: 20px; }

  .hiring {
    position: absolute; left: 83px; top: 419px; width: 116px; height: 23px;
    border-radius: 12px; background: var(--black); border: 2px solid var(--gold);
    color: #e9e9e9; font-weight: 900; font-size: 13px; line-height: 19px; text-align: center;
    letter-spacing: 0.3px;
  }
  .ad--home .hiring { top: 421px; }

  .download {
    position: absolute; left: 34px; top: 449px; display: flex; align-items: center; gap: 10px;
  }
  .ad--home .download { top: 451px; }
  .download__label { color: var(--white); font-size: 10px; font-weight: 400; }
  .store-badge {
    display: inline-block; width: 48px; height: 15px; border-radius: 3px;
    border: 1px solid #8a8a8a; background: #111;
  }

  .pitch {
    position: absolute; left: 290px; width: 152px; top: 316px; text-align: center;
    color: var(--white); font-weight: 800; font-size: 12.5px; line-height: 16px;
  }
  .ad--home .pitch { top: 318px; }

  .income {
    position: absolute; left: 286px; width: 169px; top: 374px; text-align: center;
    color: var(--ink);
  }
  .income__lead { font-weight: 700; font-size: 10.5px; line-height: 1.25; letter-spacing: 0.3px; margin-top: 13px; }
  .income__amount {
    display: block; margin: 3px 4px; height: 24px; border-radius: 12px;
    background: var(--white); border: 2px solid var(--gold-light);
    color: var(--green-dark); font-weight: 900; font-size: 18px; line-height: 20px;
  }
  .income__tail { font-weight: 700; font-size: 10.5px; line-height: 1.25; letter-spacing: 0.3px; }
</style>
</head>
<body>
<main class="ad-sheet">

  <!-- ============ MASSAGE ============ -->
  <section class="ad ad--massage">
    <svg class="ad__shapes" viewBox="0 0 475 475">
      <defs>
        <linearGradient id="band-m" x1="0" y1="0" x2="0" y2="1">
          <stop offset="0" stop-color="#22c83f"/><stop offset="0.55" stop-color="#14b334"/><stop offset="1" stop-color="#0c7f25"/>
        </linearGradient>
        <linearGradient id="gold-m" x1="0" y1="0" x2="0" y2="1">
          <stop offset="0" stop-color="#f1dc8e"/><stop offset="0.5" stop-color="#c9a544"/><stop offset="1" stop-color="#8d6d1c"/>
        </linearGradient>
        <linearGradient id="photo-m" x1="0" y1="0" x2="1" y2="1">
          <stop offset="0" stop-color="#6b5444"/><stop offset="0.5" stop-color="#c9a58a"/><stop offset="1" stop-color="#ede6df"/>
        </linearGradient>
      </defs>
      <rect x="0" y="225" width="475" height="3" fill="#c9a544"/>
      <rect x="0" y="228" width="475" height="200" fill="url(#band-m)"/>
      <circle cx="345" cy="133" r="172" fill="#c9a544"/>
      <circle cx="345" cy="133" r="166" fill="#14b334"/>
      <rect x="266" y="192" width="70" height="13" rx="6.5" fill="#14b334" stroke="#c9a544" stroke-width="2"/>
      <rect x="288" y="222" width="60" height="12" rx="6" fill="#14b334" stroke="#c9a544" stroke-width="2"/>
      <circle cx="345" cy="133" r="140" fill="url(#photo-m)" role="img" aria-label="Photo of a massage therapist giving a back massage to a client at home"/>
      <rect x="0" y="426" width="475" height="3" fill="#c9a544"/>
      <rect x="0" y="429" width="475" height="46" fill="#050505"/>
      <path d="M286 382 q0 -8 8 -8 h153 q8 0 8 8 v93 h-169 z" fill="url(#gold-m)"/>
    </svg>
    <div class="phone"><span class="phone__speaker"></span><div class="phone__screen"><div class="brand"><span class="brand__dot"></span><span class="brand__name">VANTORO</span></div></div><span class="phone__button"></span></div>
    <h2 class="headline">
      <span class="headline__line headline__kicker">PROFESSIONAL</span>
      <span class="headline__line headline__line--1">MASSAGE</span>
      <span class="headline__line headline__line--2">THERAPIST</span>
    </h2>
    <div class="at-home">AT YOUR HOME</div>
    <div class="hiring">HIRING NOW</div>
    <div class="download"><span class="download__label">Download the app now</span><span class="store-badge"></span><span class="store-badge"></span></div>
    <p class="pitch">Fastest growing<br>Canadian<br>online marketplace</p>
    <div class="income"><p class="income__lead">EARNING A SIDE INCOME<br>UP TO</p><strong class="income__amount">50K PER YEAR</strong><p class="income__tail">AND ALSO TO BE YOUR<br>OWN BOSS!</p></div>
  </section>

  <!-- ============ HAIR ============ -->
  <section class="ad ad--hair">
    <svg class="ad__shapes" viewBox="0 0 475 475">
      <defs>
        <linearGradient id="band-h" x1="0" y1="0" x2="0" y2="1">
          <stop offset="0" stop-color="#22c83f"/><stop offset="0.55" stop-color="#14b334"/><stop offset="1" stop-color="#0c7f25"/>
        </linearGradient>
        <linearGradient id="gold-h" x1="0" y1="0" x2="0" y2="1">
          <stop offset="0" stop-color="#f1dc8e"/><stop offset="0.5" stop-color="#c9a544"/><stop offset="1" stop-color="#8d6d1c"/>
        </linearGradient>
        <linearGradient id="photo-h" x1="0" y1="0" x2="1" y2="1">
          <stop offset="0" stop-color="#e9e4df"/><stop offset="0.55" stop-color="#8a8580"/><stop offset="1" stop-color="#2a2a30"/>
        </linearGradient>
      </defs>
      <rect x="0" y="225" width="475" height="3" fill="#c9a544"/>
      <rect x="0" y="228" width="475" height="200" fill="url(#band-h)"/>
      <circle cx="345" cy="133" r="172" fill="#c9a544"/>
      <circle cx="345" cy="133" r="166" fill="#14b334"/>
      <rect x="266" y="192" width="70" height="13" rx="6.5" fill="#14b334" stroke="#c9a544" stroke-width="2"/>
      <rect x="288" y="222" width="60" height="12" rx="6" fill="#14b334" stroke="#c9a544" stroke-width="2"/>
      <circle cx="345" cy="133" r="140" fill="url(#photo-h)" role="img" aria-label="Photo of a hair stylist cutting a client's hair at home"/>
      <rect x="0" y="426" width="475" height="3" fill="#c9a544"/>
      <rect x="0" y="429" width="475" height="46" fill="#050505"/>
      <path d="M286 378 q0 -8 8 -8 h153 q8 0 8 8 v97 h-169 z" fill="url(#gold-h)"/>
    </svg>
    <div class="phone"><span class="phone__speaker"></span><div class="phone__screen"><div class="brand"><span class="brand__dot"></span><span class="brand__name">VANTORO</span></div></div><span class="phone__button"></span></div>
    <h2 class="headline">
      <span class="headline__line headline__kicker">PROFESSIONAL</span>
      <span class="headline__line headline__line--1">HAIR</span>
      <span class="headline__line headline__line--2">STYLISTS</span>
    </h2>
    <div class="at-home">AT YOUR HOME</div>
    <div class="hiring">HIRING NOW</div>
    <div class="download"><span class="download__label">Download the app now</span><span class="store-badge"></span><span class="store-badge"></span></div>
    <p class="pitch">Fastest growing<br>Canadian<br>online marketplace</p>
    <div class="income" style="top:370px"><p class="income__lead">EARNING A SIDE INCOME<br>UP TO</p><strong class="income__amount">50K PER YEAR</strong><p class="income__tail">AND ALSO TO BE YOUR<br>OWN BOSS!</p></div>
  </section>

  <!-- ============ TUTORS ============ -->
  <section class="ad ad--tutors">
    <svg class="ad__shapes" viewBox="0 0 475 475">
      <defs>
        <linearGradient id="band-t" x1="0" y1="0" x2="0" y2="1">
          <stop offset="0" stop-color="#22c83f"/><stop offset="0.55" stop-color="#14b334"/><stop offset="1" stop-color="#0c7f25"/>
        </linearGradient>
        <linearGradient id="gold-t" x1="0" y1="0" x2="0" y2="1">
          <stop offset="0" stop-color="#f1dc8e"/><stop offset="0.5" stop-color="#c9a544"/><stop offset="1" stop-color="#8d6d1c"/>
        </linearGradient>
        <linearGradient id="photo-t" x1="0" y1="0" x2="1" y2="1">
          <stop offset="0" stop-color="#8a5a3c"/><stop offset="0.5" stop-color="#c9a17f"/><stop offset="1" stop-color="#9fd0d2"/>
        </linearGradient>
      </defs>
      <rect x="0" y="225" width="475" height="3" fill="#c9a544"/>
      <rect x="0" y="228" width="475" height="200" fill="url(#band-t)"/>
      <circle cx="345" cy="133" r="172" fill="#c9a544"/>
      <circle cx="345" cy="133" r="166" fill="#14b334"/>
      <rect x="266" y="192" width="70" height="13" rx="6.5" fill="#14b334" stroke="#c9a544" stroke-width="2"/>
      <rect x="288" y="222" width="60" height="12" rx="6" fill="#14b334" stroke="#c9a544" stroke-width="2"/>
      <circle cx="345" cy="133" r="140" fill="url(#photo-t)" role="img" aria-label="Photo of a smiling tutor with a student at home"/>
      <rect x="0" y="426" width="475" height="3" fill="#c9a544"/>
      <rect x="0" y="429" width="475" height="46" fill="#050505"/>
      <path d="M286 382 q0 -8 8 -8 h153 q8 0 8 8 v93 h-169 z" fill="url(#gold-t)"/>
    </svg>
    <div class="phone"><span class="phone__speaker"></span><div class="phone__screen"><div class="brand"><span class="brand__dot"></span><span class="brand__name">VANTORO</span></div></div><span class="phone__button"></span></div>
    <h2 class="headline">
      <span class="headline__line headline__kicker">PROFESSIONAL</span>
      <span class="headline__line headline__line--1">ART &amp; SCIENCE</span>
      <span class="headline__line headline__line--2">TUTORS</span>
    </h2>
    <div class="at-home">AT YOUR HOME</div>
    <div class="hiring">HIRING NOW</div>
    <div class="download"><span class="download__label">Download the app now</span><span class="store-badge"></span><span class="store-badge"></span></div>
    <p class="pitch">Fastest growing<br>Canadian<br>online marketplace</p>
    <div class="income"><p class="income__lead">EARNING A SIDE INCOME<br>UP TO</p><strong class="income__amount">50K PER YEAR</strong><p class="income__tail">AND ALSO TO BE YOUR<br>OWN BOSS!</p></div>
  </section>

  <!-- ============ HOME SERVICES ============ -->
  <section class="ad ad--home">
    <svg class="ad__shapes" viewBox="0 0 475 475">
      <defs>
        <linearGradient id="band-s" x1="0" y1="0" x2="0" y2="1">
          <stop offset="0" stop-color="#22c83f"/><stop offset="0.55" stop-color="#14b334"/><stop offset="1" stop-color="#0c7f25"/>
        </linearGradient>
        <linearGradient id="gold-s" x1="0" y1="0" x2="0" y2="1">
          <stop offset="0" stop-color="#f1dc8e"/><stop offset="0.5" stop-color="#c9a544"/><stop offset="1" stop-color="#8d6d1c"/>
        </linearGradient>
        <linearGradient id="photo-s" x1="0" y1="0" x2="1" y2="0">
          <stop offset="0" stop-color="#3a4656"/><stop offset="0.33" stop-color="#d9dde3"/><stop offset="0.6" stop-color="#e9ede8"/><stop offset="1" stop-color="#2346a8"/>
        </linearGradient>
      </defs>
      <rect x="0" y="225" width="475" height="3" fill="#c9a544"/>
      <rect x="0" y="228" width="475" height="200" fill="url(#band-s)"/>
      <circle cx="345" cy="133" r="172" fill="#c9a544"/>
      <circle cx="345" cy="133" r="166" fill="#14b334"/>
      <rect x="266" y="192" width="70" height="13" rx="6.5" fill="#14b334" stroke="#c9a544" stroke-width="2"/>
      <rect x="288" y="222" width="60" height="12" rx="6" fill="#14b334" stroke="#c9a544" stroke-width="2"/>
      <circle cx="345" cy="133" r="140" fill="url(#photo-s)" role="img" aria-label="Three photos side by side: a worker clearing snow with a snow blower, a house cleaner with a mop, and a mechanic tuning up a car"/>
      <rect x="0" y="426" width="475" height="3" fill="#c9a544"/>
      <rect x="0" y="429" width="475" height="46" fill="#050505"/>
      <path d="M286 384 q0 -8 8 -8 h153 q8 0 8 8 v91 h-169 z" fill="url(#gold-s)"/>
    </svg>
    <div class="phone"><span class="phone__speaker"></span><div class="phone__screen"><div class="brand"><span class="brand__dot"></span><span class="brand__name">VANTORO</span></div></div><span class="phone__button"></span></div>
    <h2 class="headline">
      <span class="headline__line headline__kicker">PROFESSIONAL</span>
      <span class="headline__line headline__line--1">SNOW BLOWERS,</span>
      <span class="headline__line headline__line--2">CLEANERS &amp; TUNE UP</span>
      <span class="headline__line headline__line--3">TECHNICIANS</span>
    </h2>
    <div class="at-home">AT YOUR HOME</div>
    <div class="hiring">HIRING NOW</div>
    <div class="download"><span class="download__label">Download the app now</span><span class="store-badge"></span><span class="store-badge"></span></div>
    <p class="pitch">Fastest growing<br>Canadian<br>online marketplace</p>
    <div class="income" style="top:376px"><p class="income__lead">EARNING A SIDE INCOME<br>UP TO</p><strong class="income__amount">50K PER YEAR</strong><p class="income__tail">AND ALSO TO BE YOUR<br>OWN BOSS!</p></div>
  </section>

</main>
</body>
</html>
```